Birchford Realty Business Card

Business Card:

Somewhere on front of card, please include Broker License Number: 5839162

Website is BirchfordRealty.example

Address is:
7218 Crestover Ave E
Saginaw, MI 48271

I'll let you use creative freedom on the rest; we obviously need Name, Title, Email (@BirchfordRealty.example), Office Phone, Cell Phone.

Don't want any special die-cutting, just a standard size business card.

On the back, include a place for the date and time of an appointment to be written in pen.

Requirements
Must have
• Our logo, attached to email.

```html
<!DOCTYPE html>
<html lang="en">
<head>
<meta charset="utf-8">
<title>Birchford Realty Business Card</title>
<link rel="stylesheet" href="https://fonts.googleapis.com/css2?family=Roboto+Condensed:wght@300;400;700&display=swap">
<style>
  :root {
    --navy: #2a2a72;
    --silver: #c9c9ce;
    --ink: #1b1b1b;
    --paper: #ffffff;
    --edge: #111111;
  }
  * { box-sizing: border-box; margin: 0; padding: 0; }
  html, body { width: 991px; height: 1200px; overflow: hidden; background: var(--paper); }
  body { position: relative; font-family: "Roboto Condensed", "Arial Narrow", sans-serif; color: var(--ink); }

  .card {
    position: absolute;
    left: 40px;
    width: 893px;
    height: 512px;
    background: var(--paper);
    border: 2px solid var(--edge);
    box-shadow: 6px 8px 7px rgba(0, 0, 0, 0.35);
    overflow: hidden;
  }
  .card--front { top: 44px; }
  .card--back { top: 617px; }

  /* Front */
  .identity { position: absolute; left: 28px; top: 26px; }
  .identity__name { font-size: 52px; font-weight: 300; line-height: 1; letter-spacing: 0.5px; }
  .identity__title { font-size: 35px; font-weight: 300; line-height: 1; margin-top: 6px; }
  .license { position: absolute; left: 31px; bottom: 24px; font-size: 19px; font-weight: 300; }

  .brand-panel {
    position: absolute;
    left: 355px; top: 0; right: 0; bottom: 0;
    background: var(--navy);
  }
  .contact {
    position: absolute;
    right: 40px; top: 30px;
    text-align: right;
    list-style: none;
    color: var(--silver);
    font-size: 29px;
    font-weight: 300;
    line-height: 39.5px;
  }
  .wordmark {
    position: absolute;
    right: 48px;
    font-weight: 700;
    line-height: 0.95;
    text-align: right;
  }
  .wordmark--front { bottom: 40px; color: var(--paper); font-size: 62px; }
  .wordmark--back { bottom: 40px; right: 60px; color: var(--navy); font-size: 54px; }

  /* Back */
  .appointment { position: absolute; left: 48px; top: 236px; }
  .appointment__heading { font-size: 37px; font-weight: 700; letter-spacing: 0.5px; }
  .appointment__field {
    display: flex; align-items: flex-end;
    font-size: 31px; font-weight: 300;
    margin-top: 38px;
  }
  .appointment__field:first-of-type { margin-top: 34px; }
  .appointment__line {
    display: inline-block;
    width: 300px; height: 0;
    border-bottom: 1.5px solid var(--ink);
    margin-left: 2px; margin-bottom: 5px;
  }
</style>
</head>
<body>

<section class="card card--front" aria-label="Business card front">
  <div class="identity">
    <h1 class="identity__name">Name</h1>
    <p class="identity__title">Title</p>
  </div>
  <p class="license">Broker License Number: 5839162</p>

  <div class="brand-panel">
    <ul class="contact">
      <li>7218 Crestover Ave E</li>
      <li>Saginaw, MI 48271</li>
      <li>P 000-000-0000</li>
      <li>C 000-000-0000</li>
      <li>name@birchfordrealty.example</li>
      <li>www.birchfordrealty.example</li>
    </ul>
    <p class="wordmark wordmark--front">Birchford<br>Realty</p>
  </div>
</section>

<section class="card card--back" aria-label="Business card back">
  <div class="appointment">
    <h2 class="appointment__heading">APPOINTMENT</h2>
    <p class="appointment__field">Date<span class="appointment__line"></span></p>
    <p class="appointment__field">Time<span class="appointment__line"></span></p>
  </div>
  <p class="wordmark wordmark--back">Birchford<br>Realty</p>
</section>

</body>
</html>
```